Baby Care Print Log for Nannies and Parents- Creating a brand/style I can use across different forms

I am creating a notebook for babysitters to use to communicate with parents about the children they care for. I will be creating many different forms (emergency contacts, daily logs, shopping lists, etc.)
I need a look and feel from which to style these forms from. I am starting by designing the daily baby care log. I need a designer to take my Word doc with just text on it, and create a visual approach to make this visually appealing.
I do not want this to be extremely "babyish" with cartoon styling. I want it to be more of a professional looking style. I would like to be able to color each different document a different color palette, yet keep the similar look and feel. My logo is attached for inspiration. I use real photography across my website velmorapath.com.
Updates
I will be re-designing my Wordpress website based on what design I like best and also will need other forms completed once I pick a design. I am hoping to work with someone who I can hire for further development needs as well. Added Saturday, February 11, 2017
Target Market(s)
Professional Parents
Industry/Entity Type
Education
Requirements
Must have
- color, pop, visual appeal
- Please use the color in my logo and any complementary colors that you think work well with it. I definitely like colored patterns, ombre, colored backgrounds, etc. I'd prefer for it not to be completely white with only pops of color here and there.
Nice to have
- My logo somewhere subtly on the form
- Photography elements
Should not have
- cartoon images of babies, etc. I use real photography across my website with the exception of my logo umbrella.

```html
<!DOCTYPE html>
<html lang="en">
<head>
<meta charset="utf-8">
<title>Velmora Path Notes – Daily Baby Care Log</title>
<link href="https://fonts.googleapis.com/css2?family=Roboto:wght@400;500;700&display=swap" rel="stylesheet">
<style>
  :root{
    --sky:#3ec3e0;
    --deep:#22a9c4;
    --pale:#e8f7fc;
    --mid:#c3e8f2;
    --ink:#333a3f;
    --muted:#6a7378;
    --stage:#e9eaeb;
    --paper:#ffffff;
  }
  *{box-sizing:border-box;margin:0;padding:0}
  html,body{width:1200px;height:1000px;overflow:hidden}
  body{background:var(--stage);font-family:"Roboto",Arial,sans-serif;color:var(--ink);position:relative}
  .sheet{position:absolute;left:240px;top:10px;width:720px;height:980px;background:var(--paper);overflow:hidden;box-shadow:0 6px 24px rgba(0,0,0,.12)}
  .abs{position:absolute}
  .band{position:absolute;left:0;width:720px}
  .band--top{top:0;height:120px}
  .band--bottom{bottom:0;height:100px}
  .photo{position:absolute;background:linear-gradient(145deg,#f4e3d6,#e7c4ac 60%,#f7efe9)}
  .photo--top{left:40px;top:120px;width:150px;height:130px}
  .photo--corner{right:24px;top:560px;width:170px;height:150px}
  .brand{left:230px;top:135px;display:flex;align-items:center;gap:12px}
  .brand__dot{width:30px;height:30px;border-radius:50%;background:var(--sky)}
  .brand__name{font-size:38px;font-weight:700;color:var(--ink);line-height:44px}
  .field{display:flex;align-items:flex-end;gap:8px;font-size:13px;font-weight:700;color:var(--deep)}
  .field__line{border-bottom:1.5px dotted var(--sky);height:12px}
  .log-table{position:absolute;width:300px;border-collapse:collapse;font-size:12px;outline:1.5px solid var(--sky)}
  .log-table th{background:var(--sky);color:#fff;font-weight:700;font-size:14px;padding:5px 0;text-align:center}
  .log-table .log-table__sub td{background:var(--sky);color:#fff;font-size:11px;padding:2px 10px}
  .log-table td{height:22px;border-right:1.5px solid var(--sky)}
  .log-table td:last-child{border-right:none}
  .log-table tr:nth-child(odd) td{background:var(--pale)}
  .log-table tr:nth-child(even) td{background:var(--mid)}
  .section-title{font-size:16px;font-weight:700;color:var(--deep);line-height:19px}
  .mood{left:380px;top:430px}
  .mood__grid{display:grid;grid-template-columns:repeat(4,70px);row-gap:10px;margin-top:10px}
  .mood__item{display:flex;flex-direction:column;align-items:center;font-size:11px;color:var(--muted);gap:3px}
  .mood__icon{width:26px;height:26px;border-radius:50%;background:var(--sky);border:3px solid var(--pale);box-shadow:0 0 0 1px var(--sky)}
  .diapers{left:40px;top:548px}
  .diapers__grid{display:grid;grid-template-columns:60px repeat(6,62px);row-gap:8px;align-items:center;margin-top:8px;font-size:12px;line-height:16px;color:var(--muted)}
  .diapers__time{border-bottom:1.5px dotted var(--sky);height:14px;width:48px}
  .check{width:22px;height:16px;border:1.5px solid var(--sky);border-radius:2px}
  .lines{display:flex;flex-direction:column;gap:20px}
  .lines span{display:block;border-bottom:1.5px dotted var(--sky)}
  .activities{left:40px;top:660px;width:460px}
  .supplies{left:40px;top:728px;width:640px}
  .supplies__cols{display:grid;grid-template-columns:220px 200px 200px;margin-top:6px;font-size:12px;line-height:16px;color:var(--muted)}
  .notes{left:40px;top:815px;width:560px}
</style>
</head>
<body>
<div class="sheet">
  <svg class="band band--top" viewBox="0 0 720 120" preserveAspectRatio="none" aria-hidden="true">
    <polygon points="240,0 720,0 720,70" fill="var(--sky)"/>
    <polygon points="420,0 720,0 720,38" fill="var(--deep)"/>
  </svg>

  <div class="photo photo--top" role="img" aria-label="Photograph of a smiling baby lying on its tummy"></div>

  <div class="abs brand">
    <span class="brand__dot"></span>
    <span class="brand__name">Velmora Path Notes</span>
  </div>

  <div class="abs field" style="left:380px;top:205px"><span>Date:</span><span class="field__line" style="width:240px"></span></div>
  <div class="abs field" style="left:40px;top:262px"><span>Name:</span><span class="field__line" style="width:250px"></span></div>

  <table class="log-table" style="left:40px;top:290px">
    <tr><th colspan="2">Nap Time</th></tr>
    <tr class="log-table__sub"><td style="width:80px">Time</td><td>How Long</td></tr>
    <tr><td></td><td></td></tr><tr><td></td><td></td></tr><tr><td></td><td></td></tr>
    <tr><td></td><td></td></tr><tr><td></td><td></td></tr><tr><td></td><td></td></tr>
  </table>

  <table class="log-table" style="left:380px;top:235px">
    <tr><th colspan="2">Feeding</th></tr>
    <tr class="log-table__sub"><td style="width:80px">Time</td><td>What</td></tr>
    <tr><td></td><td></td></tr><tr><td></td><td></td></tr><tr><td></td><td></td></tr>
    <tr><td></td><td></td></tr><tr><td></td><td></td></tr><tr><td></td><td></td></tr>
  </table>

  <div class="abs mood">
    <div class="section-title">Mood</div>
    <div class="mood__grid">
      <div class="mood__item"><span class="mood__icon"></span>Happy</div>
      <div class="mood__item"><span class="mood__icon"></span>Sad</div>
      <div class="mood__item"><span class="mood__icon"></span>Unsettled</div>
      <div class="mood__item"><span class="mood__icon"></span>Quiet</div>
      <div class="mood__item"><span class="mood__icon"></span>Energetic</div>
      <div class="mood__item"><span class="mood__icon"></span>Tired</div>
      <div class="mood__item"><span class="mood__icon"></span>Chatty</div>
    </div>
  </div>

  <div class="abs diapers">
    <div class="section-title">Diapers</div>
    <div class="diapers__grid">
      <span>Time</span><span class="diapers__time"></span><span class="diapers__time"></span><span class="diapers__time"></span><span class="diapers__time"></span><span class="diapers__time"></span><span class="diapers__time"></span>
      <span>Wet</span><span class="check"></span><span class="check"></span><span class="check"></span><span class="check"></span><span class="check"></span><span class="check"></span>
      <span>BM</span><span class="check"></span><span class="check"></span><span class="check"></span><span class="check"></span><span class="check"></span><span class="check"></span>
    </div>
  </div>

  <div class="photo photo--corner" role="img" aria-label="Photograph of a laughing baby propped on its arms"></div>

  <div class="abs activities">
    <div class="section-title">Today's Activities</div>
    <div class="lines" style="margin-top:10px"><span></span><span></span></div>
  </div>

  <div class="abs supplies">
    <div class="section-title">Supplies Needed Soon</div>
    <div class="supplies__cols">
      <div>Diapers<br>Diaper Cream<br>Other:</div>
      <div>Milk/Formula<br>Cereal</div>
      <div>Wet Wipes<br>Baby Food</div>
    </div>
  </div>

  <div class="abs notes">
    <div class="section-title">Special Notes</div>
    <div class="lines" style="margin-top:10px"><span></span><span></span></div>
  </div>

  <svg class="band band--bottom" viewBox="0 0 720 100" preserveAspectRatio="none" aria-hidden="true">
    <polygon points="0,100 0,60 720,20 720,100" fill="var(--sky)"/>
    <polygon points="0,100 0,85 720,70 720,100" fill="var(--deep)"/>
  </svg>
</div>
</body>
</html>
```